Sabor Callejón, Mexican Restaurant Menu

We need a menu design for a Mexican Restaurant in Dubai UAE

The concept of the Restaurant is as a Mexican Taqueria, That is simple street food like tacos, burritos, quesadillas, etc

We want a menu that is fun to read and that keeps a casual / street / urban feeling.If possible on a single page or 2 maximum so we can print on both sides and have it laminated

We are attaching photos of our logo and of the food that we will be serving, we are open to ideas and suggestions to try to make this as fun/casual as possible.

Also attaching photos of the style of tables we will use at the restaurant

Please avoid using tex mex items, like Crispy Taco Shells, Chiili, Cheddar Cheese , Fajitas, etc

Prices are not yet decided in the meantime you can use any price for the menu items.

If you can not include a photo for any single item on the menu, or you think it wouldn't look good, the ones that must be are.

1.-Tacos Al Pastor (this is the star of the show)
2-Guacamole
3-Burritos
4- Some Specials and alambres (photos attached)

Menu Items should have the description of ingredients on english and spanish (attached in menu file)

Any other idea or phrase trying to keep it fun and to show people that this is authentic mexican food and not tex mex would be nice to have.

If you have any doubts please contact us! Thanks for your help!

Target Market(s)

Expats living in Dubai + Latin Community,

Industry/Entity Type

Mexican Restaurant

Font styles to use
Other font styles liked:
• Helsinki, Helvetica , Klinic Slab

Colors
33a6d7
ec1f27
0455a3
fbee3d
9bcb3b
cadf82
f59195
85cae6
e34297

Requirements
Must have
• Fun to read, Preference on a Single page or 2 so we can print on both sides Or a Tri Fold so we can also use it for our Home Delivery Take away menu. Photos , Item ingredients in Spanish/English (attached on the menu file)
Nice to have
• Fun phrases, Reference to mexican food or characters
Should not have
• Tex Mex Items like Taco Shells , Chiili con Carne, Cheddar cheese

```html
<!DOCTYPE html>
<html lang="en">
<head>
<meta charset="utf-8">
<title>Sabor Callejón – Menu</title>
<link rel="stylesheet" href="https://fonts.googleapis.com/css2?family=Lilita+One&family=Mulish:wght@400;600&display=swap">
<style>
:root{
  --backdrop:#e9e4dc;
  --cover:#242122;
  --cover-dot:#e8294a;
  --gold:#c98a2a;
  --cream:#f7e3aa;
  --cream-mid:#efd79d;
  --red:#e8294a;
  --ink:#2a2422;
  --desc:#a2641c;
  --photo-food:#b9764a;
  --photo-plate:#efe9e2;
  --skull:#e9dfd3;
  --cactus:#3a3637;
}
*{box-sizing:border-box;margin:0;padding:0}
html,body{width:1200px;height:855px;overflow:hidden;background:var(--backdrop)}
body{position:relative;font-family:"Mulish",Arial,sans-serif;color:var(--ink)}

/* cover panel */
.cover{position:absolute;left:73px;top:133px;width:243px;height:570px;background:var(--cover);overflow:hidden}
.band-top{position:absolute;left:0;right:0;top:0;height:9px;background:var(--red)}
.band-bottom{position:absolute;left:0;right:0;bottom:0;height:9px;background:var(--gold)}
.dots{position:absolute;left:6px;right:6px;height:0;border-top:2px dotted var(--cover-dot)}
.cover .dots.top{top:19px}
.cover .dots.bottom{bottom:19px;border-color:var(--gold)}
.skull-art{position:absolute;left:75px;top:110px;width:95px;height:134px;border-radius:46px 46px 30px 30px;background:radial-gradient(circle at 50% 40%,var(--skull) 55%,#e24a5a 100%)}
.brand{position:absolute;left:0;right:0;top:288px;text-align:center}
.brand-mark{display:inline-block;width:12px;height:12px;border:1.5px solid var(--red);margin-bottom:16px}
.brand-name{font-family:"Lilita One",Impact,sans-serif;font-size:21px;color:var(--red);letter-spacing:.5px;line-height:1}
.brand-tag{margin-top:8px;font-size:5.5px;font-weight:600;letter-spacing:1.6px;color:var(--red)}
.cactus-art{position:absolute;left:102px;top:444px;width:136px;height:112px;background:linear-gradient(to top,var(--cactus),rgba(58,54,55,.35));border-radius:30px 30px 0 0}

/* inside spread */
.inside{position:absolute;left:384px;top:132px;width:747px;height:577px;background:var(--cream);overflow:hidden}
.inside .band-bottom{background:var(--red)}
.inside .dots.top{top:20px}
.inside .dots.bottom{bottom:20px}
.panel-mid{position:absolute;left:259px;top:0;width:226px;height:100%;background:var(--cream-mid)}
.fold{position:absolute;top:0;height:100%;width:1px;background:rgba(150,110,50,.18)}

.section{position:absolute}
.section h2{font-family:"Lilita One",Impact,sans-serif;font-weight:400;color:var(--red);font-size:16px;line-height:1.1;letter-spacing:.3px;margin-bottom:5px}
.item{display:flex;align-items:baseline;font-size:8.6px;line-height:1.25}
.item .name{white-space:nowrap}
.item .lead{flex:1;border-bottom:1px dotted var(--ink);margin:0 2px;transform:translateY(-2px)}
.item .price{white-space:nowrap}
.item .inline{color:var(--desc)}
.desc{font-size:7.4px;line-height:1.3;color:var(--desc);margin-bottom:4px;max-width:200px}
.gap{height:4px}
.list .item{margin-bottom:1px}

.photo{position:absolute;border-radius:50%;background:radial-gradient(ellipse at 50% 50%,var(--photo-food) 0 45%,var(--photo-plate) 50% 70%,rgba(239,233,226,0) 72%)}
.photo-drinks{position:absolute;left:547px;top:412px;width:136px;height:105px;border-radius:6px;background:linear-gradient(90deg,#e0792a 0 20%,#8ac43a 20% 40%,#d92a3a 40% 60%,#f2cf2a 60% 80%,#f08a2a 80%)}
</style>
</head>
<body>

<section class="cover">
  <div class="band-top"></div>
  <div class="dots top"></div>
  <div class="skull-art" role="img" aria-label="Illustrated sugar skull with marigold eyes"></div>
  <div class="brand">
    <span class="brand-mark"></span>
    <div class="brand-name">Sabor Callejón</div>
    <div class="brand-tag">URBAN MEXICAN FOOD</div>
  </div>
  <div class="cactus-art" role="img" aria-label="Silhouettes of desert cacti"></div>
  <div class="dots bottom"></div>
  <div class="band-bottom"></div>
</section>

<section class="inside">
  <div class="panel-mid"></div>
  <div class="fold" style="left:259px"></div>
  <div class="fold" style="left:485px"></div>
  <div class="band-top"></div>
  <div class="dots top"></div>

  <div class="section" style="left:38px;top:40px;width:215px">
    <h2>La Botana/Appetizers</h2>
    <div class="item"><span class="name">Tomás's Famous Guacamole with Chips</span><span class="lead"></span><span class="price">10$</span></div>
    <div class="gap"></div>
    <div class="item"><span class="name">Queso Fundido/Melted Cheese</span><span class="lead"></span><span class="price">10$</span></div>
    <p class="desc">Plain or with Champinones/Mushrooms</p>
    <div class="item"><span class="name">Nachos</span><span class="lead"></span><span class="price">10$</span></div>
    <div class="gap"></div>
    <p class="desc">De Pastor – Tower of chips covered with cheese beans, jalapenos and our Famous Pastor</p>
    <p class="desc">De Bistek – Tower of chips covered with cheese, beans, jalapenos and Delicious Steak</p>
    <p class="desc">Tradicional– Tower of chips covered with cheese, beans, and jalapenos</p>
    <div class="item"><span class="name">Sopes</span><span class="lead"></span><span class="price">10$</span></div>
    <p class="desc">Frijol/Refried Beans, bistek/steak o pollo/chicken</p>
    <div class="item"><span class="name">Quesadillas</span><span class="lead"></span><span class="price">10$</span></div>
    <p class="desc">Tradicional/Plain, Con Pollo/Chicken o Veggie</p>
  </div>

  <div class="photo" role="img" aria-label="Photo of steak and quesadilla plates" style="left:-6px;top:248px;width:256px;height:96px"></div>

  <div class="section list" style="left:38px;top:357px;width:215px">
    <h2>Tacos</h2>
    <div class="item"><span class="name">Pastor, The authentic Mexican Taco!</span><span class="lead"></span><span class="price">10$</span></div>
    <div class="item"><span class="name">De Bistek(s)/Steak <span class="inline">Con Queso/With Cheese</span></span><span class="lead"></span><span class="price">10$</span></div>
    <div class="item"><span class="name">De Pollo/Chicken</span><span class="lead"></span><span class="price">10$</span></div>
    <div class="item"><span class="name">De Arrachera/Skirt Steak</span><span class="lead"></span><span class="price">10$</span></div>
    <div class="item"><span class="name">Con Queso/With Cheese</span><span class="lead"></span><span class="price">10$</span></div>
    <div class="item"><span class="name">De Costilla's/Beef Ribs Tacos</span><span class="lead"></span><span class="price">10$</span></div>
    <div class="item"><span class="name">Con Queso/With Cheese</span><span class="lead"></span><span class="price">10$</span></div>
    <div class="item"><span class="name">De Cecina/Marinated Beef</span><span class="lead"></span><span class="price">10$</span></div>
    <div class="item"><span class="name">De Carne Asada/Grilled Beef</span><span class="lead"></span><span class="price">10$</span></div>
    <div class="item"><span class="name">Vegetariano / Veggie <span class="inline">Con Queso/With Cheese</span></span><span class="lead"></span><span class="price">10$</span></div>
  </div>

  <div class="section" style="left:265px;top:40px;width:212px">
    <h2>Especiales/Specials</h2>
    <div class="item"><span class="name">Mula Terca</span><span class="lead"></span><span class="price">10$</span></div>
    <p class="desc">Bistek/Steak, Tocino/Beef Bacon, Queso/Cheese with Flour Tortilla</p>
    <div class="item"><span class="name">Hawiana</span><span class="lead"></span><span class="price">10$</span></div>
    <p class="desc">Pollo/Chicken, Jamon/Turkey Ham, Pina/Pineapple, Tocino/Beef Bacon, Queso/Cheese with Flour Tortilla</p>
    <div class="item"><span class="name">Gringa</span><span class="lead"></span><span class="price">10$</span></div>
    <p class="desc">Pastor, Queso/Cheese, Cebolla/Onion, Cilantro, Pina/Pineapple with Flour Tortilla</p>
  </div>

  <div class="photo" role="img" aria-label="Photo of a special with tortillas on a plate" style="left:285px;top:166px;width:145px;height:86px"></div>

  <div class="section" style="left:265px;top:280px;width:212px">
    <h2>Burritos</h2>
    <div class="item"><span class="name">El Gringo Loco</span><span class="lead"></span><span class="price">10$</span></div>
    <p class="desc">Bistek/Steak, Frijoles/Refried Beans, Lechuga/Lettuce, Tomate/Tomato, Queso/Cheese, Guacamole y Crema/Cream</p>
    <div class="item"><span class="name">El Chido</span><span class="lead"></span><span class="price">10$</span></div>
    <p class="desc">Pollo/Chicken, Frijoles/Refried Beans, Lechuga/Lettuce, Tomate/Tomato, Queso/Cheese, Guacamole y Crema/Cream</p>
    <div class="item"><span class="name">El Guapo</span><span class="lead"></span><span class="price">10$</span></div>
    <p class="desc">Arrachera/Skirt Steak, Frijoles/ Refried Beans, Queso/Cheese, Guacamole</p>
    <div class="item"><span class="name">Super Burrito</span><span class="lead"></span><span class="price">10$</span></div>
    <p class="desc">Bistek/Steak or Arrachera/Skirt Steak or Pollo/Chicken, Tocino/Beef Bacon, Frijoles/Refried Beans, Guacamole and Queso/Cheese</p>
    <div class="item"><span class="name">Vegetariano</span><span class="lead"></span><span class="price">10$</span></div>
    <p class="desc">&nbsp;All the veggies with beans and cheese</p>
  </div>

  <div class="section" style="left:493px;top:40px;width:216px">
    <h2>Alambres (Forget<br>About Fajitas!<br>This is Mexican!)</h2>
    <div class="item"><span class="name">Tradicional</span><span class="lead"></span><span class="price">10$</span></div>
    <p class="desc">Bistek/Steak, Cebolla/Onion, Pimiento/Pepper, Jamon/Turkey Ham, Tocino/Beef Bacon, Queso/Cheese with Flour Tortilla</p>
    <div class="item"><span class="name">La Ballena</span><span class="lead"></span><span class="price">10$</span></div>
    <p class="desc">Bistek/Steak, Cebolla/Onion, Pimiento/Pepper, Jamon/Turkey Ham, Tocino/Beef Bacon, Queso/Cheese with Flour Tortilla</p>
    <div class="item"><span class="name">Sarape</span><span class="lead"></span><span class="price">10$</span></div>
    <p class="desc">Bistek/Steak, Pollo/Chicken, Cebolla/Onion, Pimiento/Pepper, Jamon/Turkey Ham, Tocino/Beef Bacon, Queso/Cheese and Tomate/Tomato with Flour Tortilla</p>
    <div class="item"><span class="name">Nano</span><span class="lead"></span><span class="price">10$</span></div>
    <p class="desc">Bistek/Steak, Pastor, Cebolla/Onion, Tocino/Beef Bacon, Queso/Cheese with Flour Tortilla</p>
  </div>

  <div class="section list" style="left:493px;top:290px;width:216px">
    <h2>Drinks</h2>
    <div class="item"><span class="name">Azul Cola</span><span class="lead"></span><span class="price">10$</span></div>
    <div class="item"><span class="name">Botellitas</span><span class="lead"></span><span class="price">10$</span></div>
    <div class="item"><span class="name">Mexican Cola</span><span class="lead"></span><span class="price">10$</span></div>
    <div class="item"><span class="name">Horchata</span><span class="lead"></span><span class="price">10$</span></div>
  </div>

  <div class="photo-drinks" role="img" aria-label="Photo of five bottles of Mexican fruit sodas"></div>

  <div class="dots bottom"></div>
  <div class="band-bottom"></div>
</section>

</body>
</html>
```